Boutique startup consulting

Hello,
Me and my partner are starting a boutique consulting/ "venturing for startup" firm and want to make professional looking slides. The point of these slide are to attract Automakers's venture arms to collaborate with us. We are hoping to win clients with this presentation.

Acceptance criteria:
1. You put beautiful designs where-ever you can and make the attached slides look professional. Full freedom in designing the slides. You are the artist, please create some magic
2. The style should be innovative and state of the art. It should be with colourful designs
3. The slides should be very professional
4. We are unsure of how to present our previous experience. Please help us out
5. The first slide has gray background. you may use the original colored image and tweak it

Here is out website:
https://www.brightmoor-partners.net/

Can you please ensure that the slides are presented in the following format?

PRESENTATION
1. Starting Masterslide
2. Customized Starting Masterslide (with Topic + Customer Logo, for eg. Smart City & KLT)
3. Service Categories Masterslide /Overview ( we have 5 Categories which are shown by icon and buzzword, see https://www.brightmoor-partners.net/live/research-strategy/research-strategy.aspx, this is for eg. the Overview for the categorie “Research &Strategy”. We have 2-4 Icon per Category, other categories are Business Development,Venture Building, Expansion Advisory, Sustainable Due Diligence , see webside)
4. Subcategories & Description Masterslide
o We have 15 Subcategories, the Masterslide should just show the Icon and then 1-2 square for description with bullets, f.ex. https://www.brightmoor-partners.net/live/expansion-advisory-feasibility-analysis/feasibility-analysis.aspx
5. Team Presenting Masterslide
o Not like Website, a Masterslide where each Teammember can present him self, in bullets with Education/Business Experience/ other awards/distinction AND in Text bubbles like “Experiences and hands-on Business developer”
6. Contact ( closing Chart with contact data, liked in etc.)
7. Masterslide (free for individual content)
o Just a slide with the CI framework which can be used as Masterslide for other charts like

8. PROPOSAL Masterslide (like customized starting slide, but Proposal)
9. Background Masterslide (Text)
o A textual description
10. Value Proposition & Goals Masterslide (Text & Bullets)
o V P will be textual so for eg. text frame; Goals with 2-4 squares (text/Bullets) for sub-goals and including the tasks for these goals in bullets
11. Milestones & Timing Masterslide (Timeline , Squares & text)
o Timeline, for eg. 6 Month project, where we have 8 tasks with starting and ending
12. Free MAsterslide /Proposal
o Where we can add charts to the proposal like Conditions or Contact

To Add:
- Logo colour description
- Picture and Icons ( so they don’t need to buy new pics or look for them)

Requirements
Must have
• Please check out the slides and make them presentable

```html
<!DOCTYPE html>
<html lang="en">
<head>
<meta charset="utf-8">
<title>Brightmoor Partners – Master Slides</title>
<link rel="stylesheet" href="https://fonts.googleapis.com/css2?family=Exo+2:wght@500;600;700&family=PT+Sans:wght@400;700&display=swap">
<style>
  :root{
    --board:#474747;
    --green:#9cc63b;
    --green-dark:#7f9f2c;
    --green-line:#b5d86a;
    --ink:#3c3c3c;
    --ink-soft:#5a5a5a;
    --paper:#ffffff;
    --paper-warm:#f4f3ef;
    --grey-col:#e6e6e6;
    --grey-active:#a9a9a9;
    --grey-box:#8a8a8a;
    --footer:#3a3a3a;
    --night-1:#1f2a14;
    --night-2:#0c120a;
  }
  *{box-sizing:border-box;margin:0;padding:0}
  html,body{width:1200px;height:704px;overflow:hidden}
  body{background:var(--board);font-family:"PT Sans",sans-serif;color:var(--ink);position:relative}

  .slide{position:absolute;width:574px;height:322px;overflow:hidden;border:1px solid var(--green-line)}
  .slide--title{left:16px;top:23px}
  .slide--custom{left:608px;top:23px}
  .slide--overview{left:16px;top:364px;background:var(--paper)}
  .slide--detail{left:608px;top:364px;background:var(--paper)}

  /* cover backgrounds */
  .cover-photo{position:absolute;inset:0;
    background:linear-gradient(180deg,#2c3a1c 0%,var(--night-1) 45%,#18200f 62%,var(--night-2) 100%)}
  .brand-lockup{position:absolute;color:var(--paper);font-family:"Exo 2",sans-serif;font-weight:600;line-height:1}
  .brand-lockup .name-main{display:block;font-size:23px;letter-spacing:.4px}
  .brand-lockup .name-sub{display:block;font-size:12px;letter-spacing:5.6px;margin-top:6px}
  .brand-lockup .mark{display:block;width:26px;height:26px;border-radius:50%;background:var(--green);margin-bottom:24px}
  .slide--title .brand-lockup{left:58px;top:84px}
  .title-rule{position:absolute;left:60px;top:212px;width:46px;height:3px;background:var(--green)}
  .title-rule::after{content:"";position:absolute;left:36px;top:0;width:10px;height:3px;background:var(--paper)}
  .hero-art{position:absolute;left:432px;top:58px;width:160px;height:250px;
    background:linear-gradient(160deg,#9cc63b 0%,#6f922a 55%,#3f5a1a 100%);opacity:.9}

  .slide--custom .brand-lockup{left:117px;top:144px}
  .slide--custom .brand-mark{position:absolute;left:58px;top:148px;width:28px;height:28px;border-radius:50%;background:var(--green)}
  .divider-v{position:absolute;left:100px;top:110px;width:2px;height:92px;background:var(--paper)}
  .pattern-strip{position:absolute;left:426px;top:0;width:92px;height:100%;background:linear-gradient(180deg,#2d4417,#1c2c0f)}

  /* service sidebar */
  .sidebar{position:absolute;left:0;top:0;height:100%;background:var(--green);color:var(--paper)}
  .slide--overview .sidebar{width:157px}
  .slide--detail .sidebar{width:133px}
  .sidebar h2{font-family:"Exo 2",sans-serif;font-weight:600;font-size:13px;letter-spacing:.6px;padding:20px 0 4px 38px;border-bottom:1.5px solid var(--paper);margin-right:14px}
  .slide--detail .sidebar h2{padding-left:28px;margin-right:0}
  .service-list{list-style:none;margin-top:26px}
  .service{display:flex;align-items:center;height:40px;padding-left:34px;font-weight:700;font-size:9.5px;line-height:1.15;position:relative}
  .slide--detail .service{padding-left:24px;font-size:8.8px;height:37px}
  .service+.service::before{content:"";position:absolute;left:32px;right:14px;top:0;height:1px;background:rgba(255,255,255,.85)}
  .slide--detail .service+.service::before{left:22px;right:0}
  .service:last-child::after{content:"";position:absolute;left:32px;right:14px;bottom:0;height:1px;background:rgba(255,255,255,.85)}
  .slide--detail .service:last-child::after{left:22px;right:0}
  .service svg{width:14px;height:14px;margin-right:9px;flex:none;fill:var(--paper)}
  .service.is-active{background:var(--green-dark)}
  .service.is-active::before{display:none}
  .service.is-active+.service::before{display:none}

  /* middle column */
  .subservice-panel{position:absolute;top:0;height:100%}
  .slide--overview .subservice-panel{left:157px;width:240px;background:var(--paper-warm)}
  .slide--detail .subservice-panel{left:133px;width:160px;background:var(--grey-col)}
  .crumb{position:absolute;display:flex;align-items:center;gap:4px;font-size:5.5px;font-weight:700;color:var(--green);letter-spacing:.3px}
  .crumb::before{content:"";width:86px;height:2px;background:var(--green)}
  .slide--overview .crumb{left:157px;top:36px}
  .slide--detail .crumb{left:321px;top:28px}
  .slide--detail .crumb::before{width:50px;height:3px}

  .category-pill{position:absolute;display:flex;align-items:center;gap:6px;height:24px;padding:0 14px 0 0;border:1.5px solid var(--green);border-radius:12px;font-family:"Exo 2",sans-serif;font-weight:700;font-size:9.5px;color:var(--ink);background:var(--paper)}
  .category-pill .badge{width:24px;height:24px;border-radius:50%;background:var(--ink);margin-left:-2px;display:flex;align-items:center;justify-content:center}
  .category-pill .badge svg{width:12px;height:12px;fill:var(--green)}
  .slide--overview .category-pill{left:28px;top:72px}
  .slide--detail .category-pill{left:20px;top:18px;height:20px;font-size:8px;border-style:dashed;background:var(--grey-col)}
  .slide--detail .category-pill .badge{width:20px;height:20px}

  .subservice-list{list-style:none;position:absolute}
  .slide--overview .subservice-list{left:60px;top:116px}
  .subservice{display:flex;align-items:center;gap:10px;height:33px;font-size:10.5px;color:var(--ink-soft)}
  .subservice svg{width:20px;height:20px;fill:none;stroke:var(--green);stroke-width:1.6}
  .slide--detail .subservice-list{left:0;top:46px;width:160px}
  .slide--detail .subservice{height:29px;font-size:8.8px;gap:8px;border-bottom:1px solid #d4d4d4;margin:0 10px;padding-left:10px}
  .slide--detail .subservice svg{width:16px;height:16px}
  .slide--detail .subservice.is-active{background:var(--grey-active);color:var(--paper);margin:0;padding-left:20px;border:0}
  .slide--detail .subservice.is-active svg{stroke:var(--paper)}
  .media-placeholder{position:absolute;left:14px;top:174px;width:135px;height:118px;background:var(--grey-box)}

  /* content column */
  .content{position:absolute;font-size:6.6px;line-height:1.3;color:var(--ink)}
  .slide--overview .content{left:418px;top:33px;width:142px}
  .content h3{font-family:"Exo 2",sans-serif;font-weight:700;color:var(--green);font-size:11.5px;line-height:1.2;margin-bottom:14px}
  .content p{margin-bottom:5px}
  .bullets{list-style:none;margin-bottom:5px}
  .bullets li{position:relative;padding-left:10px;margin-bottom:3px}
  .bullets li::before{content:"";position:absolute;left:0;top:1px;border-left:5px solid var(--green);border-top:3px solid transparent;border-bottom:3px solid transparent}
  .detail-heading{position:absolute;left:321px;top:50px;display:flex;align-items:center;gap:8px;font-family:"Exo 2",sans-serif;font-weight:700;font-size:12px;color:var(--green)}
  .detail-heading svg{width:18px;height:18px;fill:none;stroke:var(--green);stroke-width:1.6}
  .content-cols{position:absolute;left:347px;top:80px;display:flex;gap:12px;font-size:6.4px;line-height:1.28}
  .content-cols .col{width:94px;text-align:justify}
  .content-cols .bullets li{text-align:left}

  /* footer */
  .footer-bar{position:absolute;left:0;bottom:7px;height:13px;background:var(--footer);color:var(--paper);display:flex;align-items:center;font-size:6px;letter-spacing:.4px;padding-right:8px}
  .footer-bar .page{background:var(--green);height:100%;width:24px;display:flex;align-items:center;justify-content:center;font-weight:700;margin-right:8px}
  .footer-bar b{font-weight:700}
  .footer-bar .current{color:var(--green);font-weight:700}
  .footer-brand{position:absolute;right:30px;bottom:9px;display:flex;align-items:center;gap:4px;font-family:"Exo 2",sans-serif;font-weight:600;font-size:7.5px;color:var(--ink-soft)}
  .footer-brand::before{content:"";width:10px;height:10px;border-radius:50%;background:var(--green)}
</style>
</head>
<body>

<svg width="0" height="0" style="position:absolute" aria-hidden="true">
  <symbol id="i-bulb" viewBox="0 0 24 24"><path d="M12 2a7 7 0 0 0-4 12.7V17h8v-2.3A7 7 0 0 0 12 2zM9 19h6v1.5H9zM10 22h4v1h-4z"/></symbol>
  <symbol id="i-anchor" viewBox="0 0 24 24"><path d="M11 2h2v3h-2zM12 5a2 2 0 1 1 0 4 2 2 0 0 1 0-4zM11 9h2v11a6 6 0 0 0 5-5h-2l3-3 3 3h-2a8 8 0 0 1-16 0H2l3-3 3 3H6a6 6 0 0 0 5 5z"/></symbol>
  <symbol id="i-flask" viewBox="0 0 24 24"><path d="M8 2h8v2h-1v5l6 11a2 2 0 0 1-2 3H5a2 2 0 0 1-2-3l6-11V4H8z"/></symbol>
  <symbol id="i-search" viewBox="0 0 24 24"><path d="M14 2a8 8 0 1 1-5.3 14L3.4 21.3 2 19.9l5.3-5.3A8 8 0 0 1 14 2zm0 3a5 5 0 1 0 0 10 5 5 0 0 0 0-10z"/></symbol>
  <symbol id="i-bag" viewBox="0 0 24 24"><path d="M8 2h8l-2 4h-4zM9 7h6c4 3 6 7 6 10a5 5 0 0 1-5 5H8a5 5 0 0 1-5-5c0-3 2-7 6-10z"/></symbol>
  <symbol id="i-doc" viewBox="0 0 24 24"><path d="M5 3h10l4 4v14H5zM8 11h8M8 14h8M8 17h5M15 3v4h4"/></symbol>
  <symbol id="i-chart" viewBox="0 0 24 24"><path d="M3 21h18M6 18v-5M10 18V9M14 18v-7M18 18V5"/></symbol>
  <symbol id="i-people" viewBox="0 0 24 24"><circle cx="8" cy="8" r="3"/><circle cx="16" cy="8" r="3"/><path d="M2 20c0-4 3-6 6-6s6 2 6 6M12 14c1-.5 2.5-.7 4-.7 3 0 6 2 6 6"/></symbol>
  <symbol id="i-rocket" viewBox="0 0 24 24"><path d="M14 3c4 0 7 3 7 7l-8 8-7-7zM6 11l-3 1 2 2M13 18l-1 3-2-2M5 19l3-3"/></symbol>
</svg>

<!-- 1 Starting master -->
<section class="slide slide--title">
  <div class="cover-photo" role="img" aria-label="Dusk city skyline with a highway and glowing network connection lines"></div>
  <div class="brand-lockup"><span class="mark"></span><span class="name-main">BRIGHTMOOR</span><span class="name-sub">PARTNERS</span></div>
  <div class="title-rule"></div>
  <div class="hero-art" role="img" aria-label="Large green key illustration area for the cover artwork"></div>
</section>

<!-- 2 Customised starting master -->
<section class="slide slide--custom">
  <div class="cover-photo" role="img" aria-label="Dusk city skyline with a highway and glowing network connection lines"></div>
  <span class="brand-mark"></span>
  <div class="divider-v"></div>
  <div class="brand-lockup"><span class="name-main">BRIGHTMOOR</span><span class="name-sub">PARTNERS</span></div>
  <div class="pattern-strip" role="img" aria-label="Vertical band of a repeating small green decorative pattern"></div>
</section>

<!-- 3 Service overview -->
<section class="slide slide--overview">
  <aside class="sidebar">
    <h2>OUR SERVICES</h2>
    <ul class="service-list">
      <li class="service is-active"><svg><use href="#i-bulb"/></svg>Research &amp;<br>Strategy</li>
      <li class="service"><svg><use href="#i-anchor"/></svg>Business<br>Development</li>
      <li class="service"><svg><use href="#i-flask"/></svg>Venture Building</li>
      <li class="service"><svg><use href="#i-search"/></svg>Sustainable Due<br>Diligence</li>
      <li class="service"><svg><use href="#i-bag"/></svg>Expansion<br>Advisory</li>
    </ul>
  </aside>
  <div class="subservice-panel">
    <div class="category-pill"><span class="badge"><svg><use href="#i-search"/></svg></span>RESEARCH &amp; STRATEGY</div>
    <ul class="subservice-list">
      <li class="subservice"><svg><use href="#i-doc"/></svg>Scenario Planning</li>
      <li class="subservice"><svg><use href="#i-people"/></svg>Market Analysis</li>
      <li class="subservice"><svg><use href="#i-chart"/></svg>Expert Survey</li>
      <li class="subservice"><svg><use href="#i-rocket"/></svg>Start-up Screening</li>
    </ul>
  </div>
  <div class="crumb">SERVICES &gt;&gt; RESEARCH &amp; STRATEGY</div>
  <div class="content">
    <h3>Research + Strategy<br>for Innovation &amp;<br>Growth.</h3>
    <p>Consectetuer elit adipiscing, sed diam nonummy ex nibh. Euismod tincidunt ut laoreet dolore magna aliquam erat.</p>
    <p>Exerci ottatation ullamcorper suscipit lobortis nisl ut nonummy aliquip exea commodo.</p>
    <ul class="bullets">
      <li>Lorem ipsum dolor sit amet laoreet aliquae ullamcorper</li>
      <li>Conseceur elit adisponti aed diam nonummy exea</li>
      <li>Euismod tincidunt ut laoreet dolore nisl adipiscing</li>
      <li>Magna aliquam erat nibh ex ead commodo laoreet</li>
      <li>Exerci tation ullamcorper suscipit lobortis diam</li>
    </ul>
  </div>
  <div class="footer-bar"><span class="page">03</span>SMART MOBILITY &amp; KLT &gt;&gt;&nbsp;<b>SERVICES</b>&nbsp;&gt;&gt;&nbsp;<span class="current">RESEARCH &amp; STRATEGY</span></div>
  <div class="footer-brand">BRIGHTMOOR PARTNERS</div>
</section>

<!-- 4 Sub-category detail -->
<section class="slide slide--detail">
  <aside class="sidebar">
    <h2>OUR SERVICES</h2>
    <ul class="service-list">
      <li class="service is-active"><svg><use href="#i-bulb"/></svg>Research &amp;<br>Strategy</li>
      <li class="service"><svg><use href="#i-anchor"/></svg>Business<br>Development</li>
      <li class="service"><svg><use href="#i-flask"/></svg>Venture Building</li>
      <li class="service"><svg><use href="#i-search"/></svg>Sustainable Due<br>Diligence</li>
      <li class="service"><svg><use href="#i-bag"/></svg>Expansion<br>Advisory</li>
    </ul>
  </aside>
  <div class="subservice-panel">
    <div class="category-pill"><span class="badge"><svg><use href="#i-search"/></svg></span>RESEARCH &amp; STRATEGY</div>
    <ul class="subservice-list">
      <li class="subservice"><svg><use href="#i-doc"/></svg>Scenario Planning</li>
      <li class="subservice"><svg><use href="#i-people"/></svg>Market Analysis</li>
      <li class="subservice"><svg><use href="#i-chart"/></svg>Expert Survey</li>
      <li class="subservice is-active"><svg><use href="#i-rocket"/></svg>Start-up Screening</li>
    </ul>
    <div class="media-placeholder"></div>
  </div>
  <div class="crumb">SERVICES &gt;&gt; RESEARCH &amp; STRATEGY &gt;&gt; START-UP SCREENING</div>
  <div class="detail-heading"><svg><use href="#i-rocket"/></svg>Start-up Screening</div>
  <div class="content-cols">
    <div class="col">
      <p>Consectetuer elit adipiscing, sed diam nonummy ex nibh. Euismod tincidunt ut laoreet dolore magna aliquam erat.</p>
      <p>Exerci ottatation ullamcorper suscipit lobortis ut nonummy aliquip exea commodo.</p>
      <ul class="bullets">
        <li>Lorem ipsum dolor sit amet laoreet aliquae ullamcorp</li>
        <li>Conseceur elit adisponti aed diam nonummy exea</li>
        <li>Euismod tincidunt ut laoreet dolore nisl adipisng</li>
        <li>Magna aliquam erat nibh ex ead commodo laoreet</li>
        <li>Exerci tation ullamcorper suscipit lobortis diam</li>
      </ul>
      <p>Exerci ottatation ullamcorper suscipit lobortis ut nonummy aliquip exea commodo</p>
    </div>
    <div class="col">
      <ul class="bullets">
        <li>Lorem ipsum dolor sit amet laoreet aliquae ullamcorp</li>
        <li>Conseceur elit adisponti aed am nonummy exea</li>
        <li>Euismod tincidunt ut laoreet dolore nisl adipisng</li>
        <li>Magna aliquam erat nibh ex ead commodo laoreet</li>
        <li>Exerci tation ullamcorper suscipit lobortis diam</li>
      </ul>
      <p>Consectetuer elit adipiscing, sed diam nonummy ex nibh. Euismod tincidunt ut laoreet dolore magna aliquam erat.</p>
      <p>Exerci ottatation ullamcorper suscipit lobortis ut nonummy aliquip exea commodo.</p>
      <p>Euismod tincidunt ut laoreet dolore magna aliquam erat.</p>
    </div>
  </div>
  <div class="footer-bar"><span class="page">04</span>SMART MOBILITY &amp; KLT &gt;&gt;&nbsp;<b>SERVICES</b>&nbsp;&gt;&gt;&nbsp;<b>RESEARCH &amp; STRATEGY</b>&nbsp;&gt;&gt;&nbsp;<span class="current">START-UP SCREENING</span></div>
  <div class="footer-brand">BRIGHTMOOR PARTNERS</div>
</section>

</body>
</html>
```